Business card for pediatric occupational therapist

I need a business card design for my independent occupational therapy company. I am a pediatric occupational therapist working with children 0-3 years of age. I would like the card to be clean (not too 'busy') and can include pictures/cartoon-like images of children, or toys such as building blocks, or other images that would be relevant to pediatric therapy. I want it to look professional but also intended to be clear that services provided are for children.
Target Market(s)
Families requiring occupational therapy services for their children (physical, emotional, social needs) - developmental delays
Industry/Entity Type
Rehabilitation
Contact Information for Business Card
Maren Tolsvik OT LLC
Maren Tolsvik, OTR/L
Occupational Therapist
maren.tolsvikOT@brindlemail.com

```html
<!DOCTYPE html>
<html lang="en">
<head>
<meta charset="utf-8">
<title>Maren Tolsvik OT LLC – Business Card</title>
<link rel="stylesheet" href="https://fonts.googleapis.com/css2?family=Noto+Sans:ital,wght@0,400;0,700;1,400&display=swap">
<style>
  :root {
    --brand-red: #ff2b2b;
    --text-red: #ee1111;
    --paper: #ffffff;
    --backdrop: #d6d6d6;
    --placeholder: #f2c9c9;
  }
  * { margin: 0; padding: 0; box-sizing: border-box; }
  html, body {
    width: 1200px;
    height: 1200px;
    overflow: hidden;
    background: var(--backdrop);
    font-family: "Noto Sans", sans-serif;
  }
  .card {
    position: absolute;
    left: 282px;
    width: 637px;
    height: 364px;
    overflow: hidden;
  }
  .card-front {
    top: 162px;
    background: var(--brand-red);
  }
  .front-title {
    position: absolute;
    top: 162px;
    left: 0;
    width: 100%;
    text-align: center;
    color: var(--paper);
    font-weight: 700;
    font-size: 25px;
    letter-spacing: 1.7px;
    white-space: nowrap;
  }
  .card-back {
    top: 687px;
    background: var(--paper);
  }
  .top-band {
    position: absolute;
    top: 0; left: 0;
    width: 100%;
    height: 16px;
    background: var(--brand-red);
  }
  .bottom-band {
    position: absolute;
    top: 270px; left: 0;
    width: 100%;
    height: 94px;
    background: var(--brand-red);
  }
  .identity {
    position: absolute;
    right: 44px;
    top: 126px;
    text-align: left;
    color: var(--text-red);
    white-space: nowrap;
  }
  .company-name, .person-name {
    font-weight: 700;
    font-size: 25px;
    line-height: 32px;
    letter-spacing: 2.6px;
  }
  .job-title {
    position: absolute;
    right: 44px;
    top: 198px;
    color: var(--text-red);
    font-size: 18px;
    letter-spacing: 1.3px;
    white-space: nowrap;
  }
  .email {
    position: absolute;
    right: 44px;
    top: 301px;
    color: var(--paper);
    font-style: italic;
    font-size: 18px;
    letter-spacing: 0.6px;
    white-space: nowrap;
  }
  .toy-illustration {
    position: absolute;
    left: 56px;
    top: 188px;
    width: 114px;
    height: 114px;
    background: var(--placeholder);
  }
</style>
</head>
<body>
  <section class="card card-front">
    <p class="front-title">Pediatric Occupational Therapist</p>
  </section>

  <section class="card card-back">
    <div class="top-band"></div>
    <div class="bottom-band"></div>
    <div class="identity">
      <p class="company-name">Maren Tolsvik OT LLC</p>
      <p class="person-name">Maren Tolsvik, OTR/L</p>
    </div>
    <p class="job-title">Occupational Therapist</p>
    <div class="toy-illustration" role="img" aria-label="Illustration of a colourful toy beach ball"></div>
    <p class="email">maren.tolsvikOT@brindlemail.com</p>
  </section>
</body>
</html>
```